Email Signature Design

I need a Email Signature design that works on all devices and platforms. I have all the logo files and information for (4) people. It needs to be clean, fresh and reflect the simplicity of our logo. Two versions will be required, one for our main company and the same one for our sister company.

Industry/Entity Type

It Company

Requirements
Must have
• -Logo, Company Name, First and Last Name, Telephone #, Email, Website,
-Icon links for Face Book, Tale, etc that can be used or removed once we have those pages up and running
-(2) same or similar designs required, one for "Brova Properties" and one for "Brova Homes"
Nice to have
• QR Code with contact info and/or maybe

```html
<!DOCTYPE html>
<html lang="en">
<head>
<meta charset="utf-8">
<title>Brova Homes – Email Signature</title>
<link href="https://fonts.googleapis.com/css2?family=Open+Sans:wght@400;700&display=swap" rel="stylesheet">
<style>
  :root {
    --page-bg: #ffffff;
    --card-bg: #ffffff;
    --card-border: #d9d9d9;
    --card-shadow: rgba(0, 0, 0, 0.14);
    --divider: #9a9a9a;
    --ink-strong: #000000;
    --ink-label: #3a3a3a;
    --ink-body: #4a4a4a;
    --link: #2f8cc4;
    --bullet: #b5b5b5;
    --social-bg: #3c7fc0;
    --social-ink: #ffffff;
  }
  * { box-sizing: border-box; margin: 0; padding: 0; }
  html, body {
    width: 1200px;
    height: 551px;
    overflow: hidden;
    background: var(--page-bg);
    font-family: "Open Sans", Arial, sans-serif;
  }
  .signature {
    position: absolute;
    left: 86px;
    top: 68px;
    width: 1028px;
    height: 392px;
    background: var(--card-bg);
    border: 2px solid var(--card-border);
    border-radius: 8px;
    box-shadow: 0 2px 6px var(--card-shadow);
  }
  .brand {
    position: absolute;
    left: 60px;
    top: 166px;
    width: 280px;
    display: flex;
    align-items: center;
    justify-content: center;
    gap: 14px;
  }
  .brand-mark {
    width: 40px;
    height: 40px;
    background: var(--ink-strong);
    flex: none;
  }
  .brand-name {
    color: var(--ink-strong);
    font-weight: 700;
    font-size: 30px;
    line-height: 40px;
    white-space: nowrap;
  }
  .divider {
    position: absolute;
    left: 394px;
    top: 42px;
    width: 2px;
    height: 302px;
    background: var(--divider);
  }
  .details {
    position: absolute;
    left: 465px;
    top: 36px;
    color: var(--ink-body);
    font-size: 22px;
  }
  .company {
    color: var(--ink-strong);
    font-weight: 700;
    font-size: 27px;
    line-height: 38px;
  }
  .role { line-height: 32px; margin-bottom: 20px; }
  .contact-line { line-height: 42px; white-space: nowrap; }
  .label { color: var(--ink-label); font-weight: 700; }
  .sep {
    display: inline-block;
    width: 8px;
    height: 8px;
    background: var(--bullet);
    margin: 0 12px;
    vertical-align: middle;
  }
  .gap { margin-left: 16px; }
  .link { color: var(--link); text-decoration: none; }
  .social {
    display: flex;
    gap: 8px;
    margin-top: 10px;
  }
  .social a {
    height: 40px;
    padding: 0 10px;
    border-radius: 8px;
    background: var(--social-bg);
    color: var(--social-ink);
    font-size: 16px;
    font-weight: 400;
    line-height: 40px;
    text-decoration: none;
  }
</style>
</head>
<body>
  <section class="signature">
    <div class="brand">
      <div class="brand-mark" aria-hidden="true"></div>
      <div class="brand-name">Brova Homes</div>
    </div>

    <div class="divider" aria-hidden="true"></div>

    <div class="details">
      <h1 class="company">BROVA HOMES</h1>
      <p class="role">Lorem Ipsum | Managing Director</p>
      <p class="contact-line">1820 North Harbor Lane<span class="sep" aria-hidden="true"></span>Easton, SA 240913</p>
      <p class="contact-line"><span class="label">Tel:</span> (555) 0142 86203 <span class="label gap">Cell:</span> (555) 0142 86203</p>
      <p class="contact-line"><span class="label">Fax:</span> (555) 0142 86203</p>
      <p class="contact-line"><span class="label">Website:</span> <a class="link" href="#">www.brova-site.com</a></p>
      <nav class="social" aria-label="Social links">
        <a href="#">Nexa</a>
        <a href="#">Orbit</a>
        <a href="#">Pulse</a>
        <a href="#">Tale</a>
        <a href="#">Callr</a>
      </nav>
    </div>
  </section>
</body>
</html>
```